GLP letterhead

We need a letterhead design for our new company based in Los Angeles called "Gold Lantern Pictures". We develop film and television projects. We work with investors, financiers, film production companies, film distribution and sales companies as well as studios. We would like to incorporate our logo (see attached) but make the letterhead simple and elegant. We need to include: logo, company address, phone number and company website.
Updates

Hello designers, Thanks for your submissions. For our letterhead, we are looking for something more simple and elegant. No heavy bars or lines. Make it feel light and clean. Not a lot of ink on the page. Use the logo and contact info but think "clean", "streamlined" and mostly white paper. Looking forward to seeing more... thanks! Gold Lantern Pictures team

Target Market(s)

Studio executives, talent agents and agencies, financiers, investors.

Industry/Entity Type

It Company

Requirements
Must have
• Gold Lantern Pictures logo (see attached). Logo may be cropped and altered appropriately for elegant letterhead design.
• Please include:
• COMPANY ADDRESS:
• Ridgeway Studio Park
• 2850 Halverson Street
• Tower Annex, 4th Floor
• Manhattan Beach, CA 90412
• COMPANY WEBSITE:
• www.goldlanternpicturesco.example
• COMPANY PHONE NUMBER:
• 310-555-0148

```html
<!DOCTYPE html>
<html lang="en">
<head>
<meta charset="utf-8">
<title>Gold Lantern Pictures — Letterhead</title>
<link rel="stylesheet" href="https://fonts.googleapis.com/css2?family=Source+Sans+3:wght@400;600&display=swap">
<style>
  :root {
    --paper: #ffffff;
    --ink: #1a1a1a;
    --soft-blue: #d7eefa;
    --glow-blue: #1ba3e0;
    --icon-blue: #1f8fd0;
    --logo-text: #1f8fd0;
  }
  * { margin: 0; padding: 0; box-sizing: border-box; }
  html, body { width: 857px; height: 1200px; overflow: hidden; background: var(--paper); }
  .letterhead {
    position: relative;
    width: 857px;
    height: 1200px;
    background: var(--paper);
    font-family: "Source Sans 3", "Myriad Pro", sans-serif;
    color: var(--ink);
  }
  .corner-tab {
    position: absolute;
    left: 0;
    top: 30px;
    width: 6px;
    height: 62px;
    background: linear-gradient(180deg, var(--glow-blue) 0%, var(--soft-blue) 100%);
  }
  .contact {
    position: absolute;
    left: 48px;
    top: 32px;
    list-style: none;
    font-size: 12.5px;
    line-height: 16px;
  }
  .contact li { display: flex; align-items: flex-start; gap: 5px; }
  .contact svg { flex: none; width: 11px; height: 11px; margin-top: 2px; fill: var(--icon-blue); }
  .contact .address-line2 { padding-left: 16px; }
  .logo-box {
    position: absolute;
    left: 660px;
    top: 1020px;
    width: 160px;
    height: 128px;
    border-radius: 8px;
    background: var(--paper);
    border: 1px solid var(--glow-blue);
    display: flex;
    flex-direction: column;
    align-items: center;
    justify-content: center;
    gap: 12px;
  }
  .logo-dot {
    width: 40px;
    height: 40px;
    border-radius: 50%;
    background: var(--soft-blue);
  }
  .logo-name {
    font-size: 14px;
    font-weight: 600;
    letter-spacing: 1.5px;
    text-transform: uppercase;
    text-align: center;
    line-height: 17px;
    color: var(--logo-text);
  }
  .footer-line {
    position: absolute;
    left: 0;
    bottom: 24px;
    width: 857px;
    height: 3px;
    background: linear-gradient(90deg, transparent 0%, var(--soft-blue) 15%, var(--glow-blue) 50%, var(--soft-blue) 85%, transparent 100%);
  }
</style>
</head>
<body>
<main class="letterhead">
  <div class="corner-tab"></div>

  <ul class="contact">
    <li>
      <svg viewBox="0 0 12 12" aria-hidden="true"><path d="M6 0.5a3.8 3.8 0 0 0-3.8 3.8C2.2 7.2 6 11.5 6 11.5s3.8-4.3 3.8-7.2A3.8 3.8 0 0 0 6 0.5zm0 5.3a1.5 1.5 0 1 1 0-3 1.5 1.5 0 0 1 0 3z"/></svg>
      <span>Ridgeway Studio Park 2850 Halverson Street Tower Annex,</span>
    </li>
    <li class="address-line2"><span>4th Floor Manhattan Beach, CA 90412</span></li>
    <li>
      <svg viewBox="0 0 12 12" aria-hidden="true"><path d="M3.2 0.8l1.6 2.4-1 1.2c.6 1.5 1.8 2.8 3.3 3.5l1.2-1 2.3 1.6-.8 2.2C5.4 10.5 1.5 6.6 1.3 1.6z"/></svg>
      <span>310-555-0148</span>
    </li>
    <li>
      <svg viewBox="0 0 12 12" aria-hidden="true"><circle cx="6" cy="6" r="5.5"/><path d="M0.8 6h10.4M6 0.5v11M6 0.5c-2.4 2.8-2.4 8.2 0 11M6 0.5c2.4 2.8 2.4 8.2 0 11" stroke="#fff" stroke-width="0.8" fill="none"/></svg>
      <span>www.goldlanternpicturesco.example</span>
    </li>
  </ul>

  <div class="logo-box">
    <div class="logo-dot"></div>
    <p class="logo-name">Gold Lantern<br>Pictures</p>
  </div>

  <div class="footer-line"></div>
</main>
</body>
</html>
```